Corvale Wines Logo /Bottle Label

We need a contemporary update of our winery logo and wine label.
We are a small family owned vineyard with cellar door sales located at Tarrington in the Maldon Ridge Wine Region in south west Victoria Australia.
Our existing logo is an illustration of our homestead including vines in front of the homestead. We wish to include a representation of the homestead, but not necessarily the grape vines. Perhaps with a splash of colour. The final design should be conservative, classy and eye catching. The design will be used for a label on our suite of wines, including our first sparkling wine.
Updates
Designers, please note we wish to incorporate a representation of the homestead in the logo/label but not simply by using the photo of the homestead. The logo/label could be a contemporary representation of the homestead by using the outline and architectural features of the homestead in the image.
We have received several designs which fall into the trap of repeating the concept of our existing logo, by simply using the photo or illustration of the homestead provided in the brief.
We wish to encourage designers to come up with a new concept for our label, but for brand continuity we also wish to incorporate a representation of the homestead. It could be a contemporary symbol, rather than the photo or illustration. We prefer not to have trees in the logo, however grape vines may work.
Reason: To all designers, we have extended our deadline by one week as we have received only a limited number of designs and several designers have indicated that they wish to submit designs however due to other commitments have not had time to prepare and submit designs.
Reason: We have now committed to designer payment, and have extended the project for 4 days to give time to designers who were waiting until we committed to payment.
Target Market(s)
Our wines are aimed at the higher end of the market. Our customers are typically middle age and older people who are wine lovers
Industry/Entity Type
Conservative
Requirements
Must have
- - Must have a representation of our homestead see attached photo and illustration, and existing wine bottle label

```html
<!DOCTYPE html>
<html lang="en">
<head>
<meta charset="utf-8">
<title>Corvale Wines – Pinot Noir Label</title>
<link rel="stylesheet" href="https://fonts.googleapis.com/css2?family=Bodoni+Moda:wght@400;500&family=Cormorant+Garamond:wght@500;600&display=swap">
<style>
  :root {
    --wine: #6b0002;
    --kraft: #e5d2bb;
    --kraft-deep: #d9c2a6;
    --paper: #ffffff;
    --cream: #f4e9dc;
  }
  * { margin: 0; padding: 0; box-sizing: border-box; }
  html, body {
    width: 1200px; height: 1000px; overflow: hidden;
    background: var(--paper);
  }
  .canvas { position: relative; width: 1200px; height: 1000px; }

  .label {
    position: absolute; left: 50px; top: 376px;
    width: 805px; height: 586px;
    background: var(--wine);
    overflow: hidden;
  }
  .band { position: absolute; left: 0; width: 100%; }
  .band--kraft {
    top: 112px; height: 277px;
    background: radial-gradient(ellipse at 40% 40%, var(--kraft) 0%, var(--kraft-deep) 100%);
  }
  .band--rule { background: var(--kraft); }
  .rule-1 { top: 394px; height: 8px; }
  .rule-2 { top: 519px; height: 8px; }
  .rule-3 { top: 538px; height: 8px; }
  .rule-4 { top: 557px; height: 8px; }

  .winery-name {
    position: absolute; top: 20px; left: 0; width: 100%;
    text-align: center;
    font-family: "Bodoni Moda", "Didot", serif;
    font-weight: 400;
    font-size: 58px;
    letter-spacing: 15px;
    color: var(--cream);
    line-height: 80px;
  }
  .winery-name .dot { font-size: 30px; vertical-align: middle; letter-spacing: 0; margin: 0 14px; }

  .homestead-frame {
    position: absolute; left: 196px; top: 128px;
    width: 418px; height: 300px;
  }

  .vintage, .varietal, .volume {
    position: absolute;
    font-family: "Cormorant Garamond", "Times New Roman", serif;
    color: var(--cream);
    font-weight: 600;
  }
  .vintage {
    top: 438px; left: 0; width: 810px; text-align: center;
    font-size: 23px;
  }
  .varietal {
    top: 466px; left: 0; width: 810px; text-align: center;
    font-size: 30px; font-variant: small-caps; letter-spacing: 1px;
  }
  .volume {
    top: 474px; right: 22px;
    font-size: 32px; font-variant: small-caps;
  }
</style>
</head>
<body>
<main class="canvas">
  <section class="label" aria-label="Corvale Wines Pinot Noir bottle label">
    <h1 class="winery-name"><span class="dot">●</span>CORVALE<span class="dot">●</span></h1>

    <div class="band band--kraft"></div>
    <div class="band band--rule rule-1"></div>
    <div class="band band--rule rule-2"></div>
    <div class="band band--rule rule-3"></div>
    <div class="band band--rule rule-4"></div>

    <svg class="homestead-frame" viewBox="0 0 418 300" aria-hidden="false">
      <defs>
        <linearGradient id="homestead-tone" x1="0" y1="0" x2="0" y2="1">
          <stop offset="0" stop-color="#ffffff"/>
          <stop offset="0.25" stop-color="#b56a6a"/>
          <stop offset="0.7" stop-color="#7a1212"/>
          <stop offset="1" stop-color="#ffffff"/>
        </linearGradient>
      </defs>
      <ellipse cx="209" cy="150" rx="205" ry="146" fill="#ffffff" stroke="var(--wine)" stroke-width="5"/>
      <ellipse cx="209" cy="150" rx="200" ry="141" fill="url(#homestead-tone)" role="img" aria-label="Two-tone illustration of the family homestead with verandah"/>
    </svg>

    <p class="vintage">2012</p>
    <p class="varietal">Pinot Noir</p>
    <p class="volume">750Ml</p>
  </section>
</main>
</body>
</html>
```